Refresh Brightwave Coursecraft

Need a new design for e-learning development and web app development site: http://brightwavecoursecraft.example. Need pages for everything on menu bar plus a training services and a web app development services pages and a better page for samples http://brightwavecoursecraft.example/samples5/.

***Must be programmed in html 5. NO CMS. No WP. No Pillar. Straight html/css.

Target Market(s)

government

Industry/Entity Type

Government

Coding

Coded - Design and coding required

Number of Pages Required

1 page

Requirements
Must have
• Must be coded in html5/css. No CMS.
• Divided so you can easily see that we offer 3 separate services:
• Live Training - E-Learning Development - Web App Development
• A way to display logos of all our clients like on bottom of this page: https://www.quorvatests.example (this is also our website so you can copy all these logos)
• List both our Denver location which is already on our website plus our office in Veltoma Plaza. Street 62 Este, 17-83. Medellín, Antioquia.
• A page like this for our web app dev services https://www.zelbrax.example/product-development
Should not have
• CMS

```html
<!DOCTYPE html>
<html lang="en">
<head>
<meta charset="utf-8">
<title>Brightwave Coursecraft</title>
<link href="https://fonts.googleapis.com/css2?family=Questrial&family=Open+Sans:wght@400;700&display=swap" rel="stylesheet">
<style>
:root{
  --blue:#1b75bb;
  --blue-dark:#15609b;
  --orange:#f7a21b;
  --grey-bg:#ebebeb;
  --text:#333;
  --muted:#555;
  --white:#fff;
  --line:#dcdcdc;
}
*{box-sizing:border-box;margin:0;padding:0}
html,body{width:1200px;height:3377px;overflow:hidden;background:var(--white)}
body{position:relative;font-family:"Questrial",sans-serif;color:var(--text)}
.abs{position:absolute}
.topline{top:0;left:0;width:1200px;height:4px;background:linear-gradient(90deg,var(--blue) 0 50%,var(--orange) 50% 100%)}
.header{top:4px;left:0;width:1200px;height:77px;background:var(--white)}
.brand{display:flex;align-items:center;gap:10px}
.brand-mark{width:46px;height:46px;border-radius:50%;background:var(--blue)}
.brand-name{font-size:21px;color:var(--orange);line-height:1;letter-spacing:.5px}
.brand-sub{font-size:9px;color:var(--blue);letter-spacing:1px;margin-top:3px}
.header .brand{position:absolute;left:175px;top:14px}
.nav{position:absolute;left:483px;top:32px;display:flex;gap:0;font-size:13px;color:#333;letter-spacing:.3px}
.nav span{margin-right:56px}
.hero{top:81px;left:0;width:1200px;height:590px;overflow:hidden}
.hero-photo{position:absolute;inset:0;background:linear-gradient(100deg,#b9b3ab 0%,#d9d4cd 40%,#8b7d70 62%,#4a4440 85%,#2e2b29 100%)}
.hero-curve{position:absolute;left:0;bottom:0}
.hero-circle{position:absolute;left:3px;top:-42px;width:400px;height:400px;border-radius:50%;background:var(--blue)}
.hero-ring{position:absolute;left:-12px;top:-30px;width:410px;height:410px;border-radius:50%;border:3px solid var(--blue)}
.hero-title{position:absolute;left:70px;top:110px;width:300px;font-size:31px;line-height:40px;color:var(--white)}
.hero-cta{position:absolute;left:121px;top:278px;width:194px;height:194px;border-radius:50%;background:var(--orange);color:var(--white);font-size:25px;text-align:center;display:flex;align-items:center;justify-content:center;line-height:31px}
.dots{position:absolute;left:511px;top:530px;display:flex;gap:4px}
.dots i{display:block;width:43px;height:4px;background:var(--white);opacity:.8}
.services{top:671px;left:0;width:1200px;height:1546px;background:var(--grey-bg)}
.section-title{position:absolute;left:0;width:1200px;text-align:center;font-size:37px;color:#222}
.section-lead{position:absolute;left:315px;width:580px;text-align:center;font-family:"Open Sans",sans-serif;font-size:11px;line-height:22px;color:var(--muted)}
.card{position:absolute;left:173px;width:851px;height:362px;background:var(--white)}
.card-img{position:absolute;top:0;width:426px;height:362px}
.card-title{position:absolute;top:34px;height:64px;padding:0 30px;background:var(--white);border-radius:32px;font-size:32px;line-height:64px;white-space:nowrap}
.card-title .o{color:var(--orange)}
.card-title .b{color:var(--blue)}
.card-text{position:absolute;top:118px;width:364px;font-family:"Open Sans",sans-serif;font-size:11px;line-height:22px;color:var(--muted)}
.btn{position:absolute;height:34px;border-radius:17px;background:var(--orange);color:var(--white);font-family:"Open Sans",sans-serif;font-weight:700;font-size:10px;text-align:center;line-height:34px;letter-spacing:.5px}
.clients{top:2217px;left:0;width:1200px;height:739px;background:var(--white)}
.client-grid{position:absolute;left:178px;top:230px;width:846px;height:362px;display:grid;grid-template-columns:repeat(5,1fr);grid-template-rows:repeat(3,1fr);border-top:1px solid var(--line);border-left:1px solid var(--line)}
.client{border-right:1px solid var(--line);border-bottom:1px solid var(--line);display:flex;align-items:center;justify-content:center;gap:8px;font-size:15px;color:#444}
.client i{display:block;width:22px;height:22px;border-radius:50%;background:var(--blue)}
.contacts{top:2956px;left:0;width:623px;height:324px;background:var(--blue);color:var(--white)}
.contacts h3{position:absolute;left:172px;top:54px;font-size:27px;font-weight:400}
.loc-title{position:absolute;top:114px;font-size:18px}
.loc-line{position:absolute;font-family:"Open Sans",sans-serif;font-size:11px;line-height:22px;display:flex;align-items:flex-start;gap:10px}
.loc-line svg{flex:none;margin-top:4px}
.map{top:2956px;left:623px;width:577px;height:324px;background:linear-gradient(90deg,#dfe4d6 0%,#e7e9df 60%,#c8dff2 78%,#aacfef 100%)}
.footer{top:3280px;left:0;width:1200px;height:97px;background:var(--white)}
.footer .brand{position:absolute;left:178px;top:25px}
.copy{position:absolute;left:478px;top:40px;font-family:"Open Sans",sans-serif;font-size:11px;color:#333}
.social{position:absolute;left:920px;top:38px;display:flex;gap:14px;font-size:13px;color:#222}
</style>
</head>
<body>
<div class="abs topline"></div>
<header class="abs header">
  <div class="brand"><span class="brand-mark"></span><div><div class="brand-name">BRIGHTWAVE</div><div class="brand-sub">COURSECRAFT</div></div></div>
  <nav class="nav"><span>HOME</span><span>SERVICES</span><span>PORTFOLIO</span><span>TEAM &amp; EXPERIENCE</span><span>CONTACTS</span></nav>
</header>

<section class="abs hero">
  <div class="hero-photo" role="img" aria-label="Photo of a learner studying at a desk in a bright office"></div>
  <svg class="hero-curve" width="1200" height="120" viewBox="0 0 1200 120"><path d="M0 0 Q600 150 1200 0 L1200 120 L0 120Z" fill="#ebebeb"/></svg>
  <div class="hero-ring"></div>
  <div class="hero-circle"></div>
  <h1 class="hero-title" style="font-weight:400">We create engaging training that exceed expectations.</h1>
  <div class="hero-cta">Get<br>Started</div>
  <div class="dots"><i></i><i></i><i></i><i></i></div>
</section>

<section class="abs services">
  <h2 class="section-title" style="top:40px;font-weight:400">Our Services</h2>
  <p class="section-lead" style="top:100px">Sed ut perspiciatis unde omnis iste natus error sit voluptatem accusantium doloremque laudantium, totam remaperiam, eaque ipsa quaeb illo inventore veritatis et quasi te natus error sit voluptatem accusantium dolorem que laudantium, totam remaperiam, eaque ipsa quaeb illo inventore veritatis et quasi architecto</p>

  <article class="card" style="top:214px">
    <div class="card-img" style="left:0;background:linear-gradient(135deg,#c9b8a4,#6d5a4c 60%,#3b332e)" role="img" aria-label="Photo of a trainer presenting to a seated audience"></div>
    <h3 class="card-title" style="left:362px;font-weight:400"><span class="o">Live</span> <span class="b">Training</span></h3>
    <p class="card-text" style="left:451px">Sed ut perspiciatis unde omnis iste natus error sit voluptatem accusa ntium doloremque laudantium, totam rem aperiam, eaque ipsa quaeb illo inventore veritatis et quasi architecto beatae vitae dicta sunt expl icabo. Nemo enim ipsam voluptatem quia voluptas sit aspernSed ut pe rspiciatis unde omnis iste natus error sit voluptatem accusantium dol oremque laudantium, totam rem aperiam, eaque ipsa quae ab illo inv entore veritatis et quasi architecto beatae.</p>
    <div class="btn" style="left:454px;top:294px;width:104px">READ MORE</div>
  </article>

  <article class="card" style="top:630px">
    <div class="card-img" style="left:426px;background:linear-gradient(135deg,#8a8f96,#4d5258 55%,#2a2d31)" role="img" aria-label="Photo of hands at a laptop with floating digital icons"></div>
    <h3 class="card-title" style="left:79px;font-weight:400"><span class="o">E-Learning</span> <span class="b">Development</span></h3>
    <p class="card-text" style="left:34px;text-align:right">Sed ut perspiciatis unde omnis iste natus error sit voluptatem accusa ntium doloremque laudantium, totam rem aperiam, eaque ipsa quaeb illo inventore veritatis et quasi architecto beatae vitae dicta sunt expl icabo. Nemo enim ipsam voluptatem quia voluptas sit aspernSed ut pe rspiciatis unde omnis iste natus error sit voluptatem accusantium dol oremque laudantium, totam rem aperiam, eaque ipsa quae ab illo inv entore veritatis et quasi architecto beatae.</p>
    <div class="btn" style="left:289px;top:290px;width:104px">READ MORE</div>
  </article>

  <article class="card" style="top:1044px">
    <div class="card-img" style="left:0;background:linear-gradient(135deg,#2f3f4d,#5b6b78 50%,#9a7a5e)" role="img" aria-label="Photo of two developers reviewing an app on a phone and monitor"></div>
    <h3 class="card-title" style="left:362px;font-weight:400"><span class="o">Web App</span> <span class="b">Development</span></h3>
    <p class="card-text" style="left:451px">Sed ut perspiciatis unde omnis iste natus error sit voluptatem accusa ntium doloremque laudantium, totam rem aperiam, eaque ipsa quaeb illo inventore veritatis et quasi architecto beatae vitae dicta sunt expl icabo. Nemo enim ipsam voluptatem quia voluptas sit aspernSed ut pe rspiciatis unde omnis iste natus error sit voluptatem accusantium dol oremque laudantium, totam rem aperiam, eaque ipsa quae ab illo inv entore veritatis et quasi architecto beatae.</p>
    <div class="btn" style="left:454px;top:290px;width:104px">READ MORE</div>
  </article>
</section>

<section class="abs clients">
  <h2 class="section-title" style="top:82px;font-weight:400">Our Clients</h2>
  <p class="section-lead" style="top:142px;width:580px">Sed ut perspiciatis unde omnis iste natus error sit voluptatem accusantium doloremque laudantium, totam remaperiam, eaque ipsa quaeb illo inventore veritatis et quasi te natus error sit voluptatem</p>
  <div class="client-grid">
    <div class="client"><i></i>Skyreach Corps</div>
    <div class="client"><i></i>Hollin Univ.</div>
    <div class="client"><i></i>Ridgeford</div>
    <div class="client"><i></i>Workpath</div>
    <div class="client">Clarivane</div>
    <div class="client"><i></i>Verdalis</div>
    <div class="client"><i></i>Lakemont</div>
    <div class="client">Oakmere College</div>
    <div class="client"><i></i>Northvale Univ.</div>
    <div class="client"><i></i>Medforma</div>
    <div class="client"><i></i>Harlow Dept.</div>
    <div class="client">Plainsview State</div>
    <div class="client"><i></i>Coastline</div>
    <div class="client"><i></i>Emberwatch</div>
    <div class="client"><i></i>Silverpeak</div>
  </div>
  <div class="btn" style="left:529px;top:622px;width:142px;height:36px;line-height:36px;border-radius:18px">VIEW ALL CLIENTS</div>
</section>

<section class="abs contacts">
  <h3>Contacts</h3>
  <div class="loc-title" style="left:172px">Location 1</div>
  <div class="loc-title" style="left:427px">Location 2</div>
  <div class="loc-line" style="left:172px;top:148px">
    <svg width="12" height="14" viewBox="0 0 12 14"><path d="M6 1a4 4 0 0 1 4 4c0 3-4 8-4 8S2 8 2 5a4 4 0 0 1 4-4z" fill="none" stroke="#fff"/><circle cx="6" cy="5" r="1.5" fill="#fff"/></svg>
    <span>5820 E Larkin Road, Suite 2-140<br>Aurora, CO 80019</span></div>
  <div class="loc-line" style="left:172px;top:196px">
    <svg width="12" height="12" viewBox="0 0 12 12"><path d="M2 1l3 0 1 3-2 1a7 7 0 0 0 3 3l1-2 3 1 0 3C6 11 1 6 2 1z" fill="none" stroke="#fff"/></svg>
    <span>Telephone: +1 555 014 7720</span></div>
  <div class="loc-line" style="left:172px;top:218px">
    <svg width="14" height="10" viewBox="0 0 14 10"><rect x=".5" y=".5" width="13" height="9" fill="none" stroke="#fff"/><path d="M.5 .5l6.5 5 6.5-5" fill="none" stroke="#fff"/></svg>
    <span>E-mail: support@brightwavecoursecraft.example</span></div>
  <div class="loc-line" style="left:427px;top:148px">
    <svg width="12" height="14" viewBox="0 0 12 14"><path d="M6 1a4 4 0 0 1 4 4c0 3-4 8-4 8S2 8 2 5a4 4 0 0 1 4-4z" fill="none" stroke="#fff"/><circle cx="6" cy="5" r="1.5" fill="#fff"/></svg>
    <span>Veltoma Plaza. Street 62 Este,<br>17-83. Medellín, Antioquia</span></div>
</section>
<div class="abs map" role="img" aria-label="Street map showing the office location with a pin"></div>

<footer class="abs footer">
  <div class="brand"><span class="brand-mark"></span><div><div class="brand-name">BRIGHTWAVE</div><div class="brand-sub">COURSECRAFT</div></div></div>
  <p class="copy">© 2019 All Rights Reserved. Privacy Policy | Terms of Use | Contact</p>
  <div class="social"><span>Feed</span><span>Page</span><span>Video</span></div>
</footer>
</body>
</html>
```